Innovative biopolymers technology company needs a professional and engaging website

KELVO Polymer Systems AG is a biopolymer technology licensing company that enables plastic compounders to access new markets and innovate, plastic converters to manufacture bio-based, biodegradable, and bio-neutral plastic, and brand owners to satisfy the end-users’ demand for ‘greener’ plastics.

Our purpose is to help mankind ‘enjoy the convenience of plastic products guilt-free’. That’s why we’ve developed and patented our MARUSTEN® Technology, which enables producing plastics that are ‘kind at heart’. Our products are based on renewable materials, up to 99%, and can be – if required – 100% biodegradable at the same time.

Technically our bio plastics could replace 90% of today’s polyethylene applications. Therefore, our vision is ‘to make MARUSTEN® the world’s standard for the production and innovation in the area of biopolymers’.

We'd like to see website designs that portray us a serious technology company, whose products benefit the environment and brings alive our brand promise of 'kind at heart'.

Target Market(s)

Our primary target audience are plastics compounders that either want to produce resin/pellets, which allow their clients to produce either bio-based or biodegradable plastic.

Industry/Entity Type

Biodegradable

Requirements
Must have
• The website should be designed that it creates the desired user experience, represents the pre-defined structure, and meets our brand guidelines (see attached document KELVO_WebsiteDesignBrief_FinalVersion.pdf). Moreover, it needs to include the prepared content (see attached document KELVO_WebsiteContent_FinalVersion.doc).
Nice to have
• Ideally the selected Wordpress template should have an ordering functionality build-in already so that at a later stage we could order a product ordering process.
Should not have
• The design shouldn't look like purely an environmental company.

```html
<!DOCTYPE html>
<html lang="en">
<head>
<meta charset="utf-8">
<title>KELVO Polymer Systems AG</title>
<link href="https://fonts.googleapis.com/css2?family=Open+Sans:ital,wght@0,400;0,600;0,700;1,400;1,600&display=swap" rel="stylesheet">
<style>
:root{
  --teal-dark:#0f6c74;
  --teal:#2bafb2;
  --teal-soft:#74c9c6;
  --footer:#74c7bf;
  --footer-deep:#65b4ad;
  --page:#f2f2f2;
  --panel:#e7e7e7;
  --card:#ffffff;
  --ink:#606b6e;
  --ink-soft:#6f7a7d;
  --heading:#6b7578;
  --nav:#147e88;
  --black:#151515;
  --white:#ffffff;
}
*{box-sizing:border-box;margin:0;padding:0}
html,body{width:993px;height:1200px;overflow:hidden}
body{font-family:"Open Sans",Arial,sans-serif;background:var(--page);color:var(--ink);position:relative}
a{color:inherit;text-decoration:none}
ul{list-style:none}

.site-header{position:absolute;left:0;top:0;width:993px;height:55px;background:var(--white);border-top:2px solid #e4e4e4}
.site-header::after{content:"";position:absolute;left:0;right:0;bottom:0;height:8px;
  background:repeating-linear-gradient(90deg,#d7d7d7 0 1px,transparent 1px 4px);}
.brand{position:absolute;left:157px;top:8px;display:flex;align-items:center;gap:7px;font-weight:700;font-size:25px;letter-spacing:1px;color:#1e1e1e}
.brand-dot{width:12px;height:12px;border-radius:50%;background:var(--teal)}
.main-nav{position:absolute;right:111px;top:19px;display:flex;font-size:9.5px;font-weight:600;color:var(--nav)}
.main-nav li{display:flex;align-items:center}
.main-nav li+li::before{content:"";width:1px;height:7px;background:var(--nav);margin:0 9px 0 11px}

.hero{position:absolute;left:0;top:55px;width:993px;height:330px;
  background:radial-gradient(ellipse at 50% 40%,#d9efb4 0%,#a6d86a 35%,#58b531 75%,#3f9e24 100%)}
.hero-title{position:absolute;left:382px;top:105px;width:229px;height:33px;background:var(--teal-dark);color:var(--white);
  font-size:32px;font-weight:700;line-height:33px;text-align:center;letter-spacing:1px;border-radius:2px}
.hero-caption{position:absolute;left:341px;top:145px;width:311px;height:46px;background:rgba(70,80,70,.72);color:#f2f2f2;
  font-size:11.3px;line-height:17px;text-align:center;padding-top:6px;border-radius:2px}
.hero-arrow{position:absolute;top:144px;width:33px;height:39px;background:#128a95;display:flex;align-items:center;justify-content:center}
.hero-arrow.prev{left:0}.hero-arrow.next{right:0}
.slider-dots{position:absolute;top:398px;left:430px;display:flex;gap:6px}
.slider-dots span{width:40px;height:3px;background:#b4b8b9}
.slider-dots .active{background:var(--teal-soft)}

.services-banner{position:absolute;left:108px;top:417px;width:774px;height:65px;background:var(--panel)}
.services-banner h2{position:absolute;left:18px;top:11px;font-size:20.5px;font-weight:400;color:var(--heading)}
.services-banner p{position:absolute;left:18px;top:40px;font-size:8.3px;color:var(--ink)}
.btn-view{position:absolute;left:619px;top:16px;width:132px;height:34px;background:var(--teal);color:var(--white);
  font-size:13.5px;font-weight:600;line-height:34px;text-align:center;border-radius:2px;box-shadow:0 2px 0 #21908f}

.service-card{position:absolute;top:516px;width:179px;height:205px;background:var(--card);box-shadow:0 2px 2px rgba(0,0,0,.07);text-align:center}
.service-card h3{font-size:11px;font-weight:700;color:var(--heading);margin-top:24px;letter-spacing:.3px}
.service-card p{font-size:8.5px;line-height:13.6px;color:var(--ink);padding:0 10px;margin-top:10px;min-height:50px}
.service-card p+p{margin-top:10px}
.btn-read{position:absolute;left:25px;top:188px;width:133px;height:35px;background:var(--teal-soft);color:var(--white);
  font-size:10px;font-weight:600;line-height:34px;border-radius:2px;box-shadow:0 2px 0 #5fb5b2}
.btn-read.dark{background:var(--black);box-shadow:none}

.why-us{position:absolute;left:108px;top:798px;width:170px}
.section-title{font-size:11px;font-weight:700;color:var(--heading)}
.why-us ul{margin-top:19px}
.why-us li{font-size:8.8px;line-height:17px;display:flex;align-items:center;gap:4px}
.intro-text{position:absolute;left:321px;top:795px;width:350px;font-size:8.4px;line-height:16px}
.intro-text a{color:#222;text-decoration:underline}
.gauges{position:absolute;left:310px;top:862px;display:flex;gap:15px}
.gauge{position:relative;width:81px;text-align:center}
.gauge svg{display:block}
.gauge-value{position:absolute;left:0;top:19px;width:81px;text-align:center;font-size:19px;font-weight:700;line-height:24px;color:#7d8689}
.gauge-label{font-size:11px;font-weight:700;color:var(--heading);margin-top:10px}
.testimonial{position:absolute;left:702px;top:798px;width:180px}
.quote{margin-top:16px;background:var(--white);padding:6px 12px 6px 12px;font-size:8.4px;line-height:16.3px;font-style:italic;height:80px;position:relative}
.quote::after{content:"";position:absolute;left:0;bottom:-20px;border-left:28px solid var(--white);border-bottom:20px solid transparent}
.quote-author{margin:6px 0 0 42px;font-size:11px;font-weight:600;color:#6d7578}

.site-footer{position:absolute;left:3px;top:967px;width:990px;height:199px;background:var(--footer);color:var(--white)}
.site-footer::before{content:"";position:absolute;left:0;right:0;top:0;height:8px;
  background:repeating-linear-gradient(90deg,rgba(255,255,255,.6) 0 1px,transparent 1px 4px)}
.footer-about{position:absolute;left:111px;top:62px;width:245px;font-size:8.4px;line-height:15.8px}
.contact{position:absolute;left:111px;top:122px;font-size:8.4px}
.contact div{display:flex;align-items:center;height:20px}
.contact span{width:40px}
.contact strong{font-size:14px;font-weight:600;font-style:italic}
.footer-col{position:absolute;top:30px}
.footer-col h4{font-size:14px;font-weight:600;color:#3f5f5f}
.footer-col ul{margin:16px 0 0 16px}
.footer-col li{font-size:8.6px;line-height:15.5px;padding-left:10px;position:relative}
.footer-col li::before{content:"›";position:absolute;left:0;top:-1px}
.footer-blog{position:absolute;left:637px;top:30px}
.footer-blog h4{font-size:14px;font-weight:400;font-style:italic}
.footer-blog h4 b{font-style:normal;font-weight:700}
.post{display:flex;gap:13px;margin-top:14px;width:240px}
.post:first-of-type{margin-top:15px}
.post-thumb{width:47px;height:46px;background:#5fa9a2;display:flex;align-items:center;justify-content:center;flex:none}
.post p{font-size:8.6px;line-height:12.5px}
.post time{display:block;font-size:8.6px;margin-top:3px}
.footer-bottom{position:absolute;left:3px;top:1166px;width:990px;height:34px;background:var(--footer-deep);color:var(--white)}
.copyright{position:absolute;left:111px;top:13px;font-size:8.4px}
.social{position:absolute;right:107px;top:10px;display:flex;gap:16px}
.social span{width:14px;height:14px;border-radius:50%;background:var(--white)}
</style>
</head>
<body>

<header class="site-header">
  <div class="brand"><span>KELVO</span><span class="brand-dot"></span></div>
  <ul class="main-nav">
    <li><a href="#">Home</a></li>
    <li><a href="#">About Us</a></li>
    <li><a href="#">Services</a></li>
    <li><a href="#">Contact Us</a></li>
  </ul>
</header>

<section class="hero" role="img" aria-label="Photograph of a teal molecular model on a bright green blurred background">
  <h1 class="hero-title">VESTIBULUM</h1>
  <p class="hero-caption">Maecenas tincidunt, augue et rutrum condimentum,<br>libero lectus mattis orci, ut commodo.</p>
  <a class="hero-arrow prev" href="#" aria-label="Previous slide"><svg width="16" height="14" viewBox="0 0 16 14"><path d="M8 1 2 7l6 6M14 1 8 7l6 6" fill="none" stroke="#fff" stroke-width="2"/></svg></a>
  <a class="hero-arrow next" href="#" aria-label="Next slide"><svg width="16" height="14" viewBox="0 0 16 14"><path d="M2 1l6 6-6 6M8 1l6 6-6 6" fill="none" stroke="#fff" stroke-width="2"/></svg></a>
</section>
<div class="slider-dots"><span></span><span class="active"></span><span></span></div>

<section class="services-banner">
  <h2>Some of our top services</h2>
  <p>Ut eleifend libero sed neque rhoncus consequat. Maecenas tincidunt, augue et rutrum condimentum, libero lectus mattis orci, ut commodo.</p>
  <a class="btn-view" href="#">VIEW MORE</a>
</section>

<article class="service-card" style="left:108px">
  <h3>SUSPENDISSE</h3>
  <p>Quisque id tellus quis risus vehicula vehicula ut turpis. In eros nulla, placerat vitae at, vehicula ut nunc.</p>
  <p>Quisque id tellus quis risus vehicula vehicula ut turpis. In eros nulla, placerat vitae at, vehicula ut nunc.</p>
  <a class="btn-read dark" href="#">read more</a>
</article>
<article class="service-card" style="left:306px">
  <h3>MAECENAS</h3>
  <p>Ut eleifend libero sed neque rhoncus consequat. Maecenas tincidunt, augue et rutrum condimentum, libero lectus mattis orci, ut commodo.</p>
  <p>Ut eleifend libero sed neque rhoncus consequat. Maecenas tincidunt, augue et rutrum condimentum, libero lectus mattis orci, ut commodo.</p>
  <a class="btn-read" href="#">read more</a>
</article>
<article class="service-card" style="left:505px">
  <h3>ALIQUAM</h3>
  <p>Vivamus eget ante bibendum arcu vehicula ultricies. Integer venenatis mattis nisl, vitae pulvinar dui tempor non.</p>
  <p>Vivamus eget ante bibendum arcu vehicula ultricies. Integer venenatis mattis nisl, vitae pulvinar dui tempor non.</p>
  <a class="btn-read" href="#">read more</a>
</article>
<article class="service-card" style="left:703px">
  <h3>HABITASSE</h3>
  <p>Astehicula ultricies. Integer venenatis mattis nisl, vitae pulvinar dui tempor non.</p>
  <p>Astehicula ultricies. Integer venenatis mattis nisl, vitae pulvinar dui tempor non.</p>
  <a class="btn-read" href="#">read more</a>
</article>

<section class="why-us">
  <h3 class="section-title">Why Choose Us ?</h3>
  <ul>
    <li><svg width="8" height="8" viewBox="0 0 8 8"><path d="M0 4h6M3.5 1 6.5 4 3.5 7" fill="none" stroke="#222" stroke-width="1.6"/></svg>Quisque at massa ipsum</li>
    <li><svg width="8" height="8" viewBox="0 0 8 8"><path d="M0 4h6M3.5 1 6.5 4 3.5 7" fill="none" stroke="#222" stroke-width="1.6"/></svg>Maecenas a lorem augue, egestas</li>
    <li><svg width="8" height="8" viewBox="0 0 8 8"><path d="M0 4h6M3.5 1 6.5 4 3.5 7" fill="none" stroke="#222" stroke-width="1.6"/></svg>Cras vitae felis at lacus eleifend</li>
    <li><svg width="8" height="8" viewBox="0 0 8 8"><path d="M0 4h6M3.5 1 6.5 4 3.5 7" fill="none" stroke="#222" stroke-width="1.6"/></svg>Etiam auctor diam pellentesque</li>
    <li><svg width="8" height="8" viewBox="0 0 8 8"><path d="M0 4h6M3.5 1 6.5 4 3.5 7" fill="none" stroke="#222" stroke-width="1.6"/></svg>Nulla ac massa at dolor</li>
    <li><svg width="8" height="8" viewBox="0 0 8 8"><path d="M0 4h6M3.5 1 6.5 4 3.5 7" fill="none" stroke="#222" stroke-width="1.6"/></svg>Condimentum eleifend vitae vitae</li>
  </ul>
</section>

<p class="intro-text">Curabitur quis nisl in leo euismod venenatis eu in diam. Etiam auctor diam pellentesque lectus <a href="#">vehicula mattis</a>. Nulla ac massa at dolor condimentum eleifend vitae vitae urna.</p>

<div class="gauges">
  <div class="gauge">
    <svg width="81" height="43" viewBox="0 0 81 43"><path d="M5 42a35.5 35.5 0 0 1 71 0" pathLength="100" fill="none" stroke="#74c9c6" stroke-width="9"/><path d="M5 42a35.5 35.5 0 0 1 71 0" pathLength="100" fill="none" stroke="#151515" stroke-width="9" stroke-dasharray="50 100"/></svg>
    <span class="gauge-value">50</span><div class="gauge-label">SUSPENDISSE</div>
  </div>
  <div class="gauge">
    <svg width="81" height="43" viewBox="0 0 81 43"><path d="M5 42a35.5 35.5 0 0 1 71 0" pathLength="100" fill="none" stroke="#74c9c6" stroke-width="9"/><path d="M5 42a35.5 35.5 0 0 1 71 0" pathLength="100" fill="none" stroke="#151515" stroke-width="9" stroke-dasharray="70 100"/></svg>
    <span class="gauge-value">70</span><div class="gauge-label">MAECENAS</div>
  </div>
  <div class="gauge">
    <svg width="81" height="43" viewBox="0 0 81 43"><path d="M5 42a35.5 35.5 0 0 1 71 0" pathLength="100" fill="none" stroke="#74c9c6" stroke-width="9"/><path d="M5 42a35.5 35.5 0 0 1 71 0" pathLength="100" fill="none" stroke="#151515" stroke-width="9" stroke-dasharray="80 100"/></svg>
    <span class="gauge-value">80</span><div class="gauge-label">ALIQUAM</div>
  </div>
  <div class="gauge">
    <svg width="81" height="43" viewBox="0 0 81 43"><path d="M5 42a35.5 35.5 0 0 1 71 0" pathLength="100" fill="none" stroke="#151515" stroke-width="9"/></svg>
    <span class="gauge-value">100</span><div class="gauge-label">HABITASSE</div>
  </div>
</div>

<section class="testimonial">
  <h3 class="section-title">What Client’s Say ?</h3>
  <blockquote class="quote">Curabitur quis nisl in leo euismod venenatis eu in diam. Etiam auctor diam pellentesque lectus <em>vehicula mattis</em>. Nulla ac massa at dolor condimentum</blockquote>
  <p class="quote-author">Mara Lindqvist</p>
</section>

<footer class="site-footer">
  <p class="footer-about">Lorem ipsum dolor sit amet, consectetur adipiscing elit. Nam viverra euismod odio, gravida pellentesque urna varius vitae. Sed dui lorem, adipiscing in adipiscing et, interdum nec .</p>
  <div class="contact">
    <div><span>Phone:</span><strong>140 3318 7724</strong></div>
    <div><span>e-mail:</span><strong>hello@kelvo-polymer.eu</strong></div>
  </div>
  <nav class="footer-col" style="left:373px">
    <h4>Company</h4>
    <ul><li>About</li><li>FAQ</li><li>Contact</li><li>Terms</li><li>Privacy</li><li>Testimonials</li></ul>
  </nav>
  <nav class="footer-col" style="left:505px">
    <h4>Community</h4>
    <ul><li>Blog</li><li>Forum</li><li>Support</li><li>Newsletter</li></ul>
  </nav>
  <section class="footer-blog">
    <h4>from the <b>BLOG</b></h4>
    <div class="post">
      <div class="post-thumb" role="img" aria-label="Blog post thumbnail"><svg width="20" height="16" viewBox="0 0 20 16"><rect x="1" y="1" width="18" height="14" fill="none" stroke="#cfe9e6" stroke-width="1.5"/><path d="M3 13l5-5 3 3 2-2 4 4z" fill="#cfe9e6"/><circle cx="14" cy="5" r="1.6" fill="#cfe9e6"/></svg></div>
      <div><p>Lorem ipsum dolor sit amet, consectetur adipiscing elit</p><time>26 May, 2013</time></div>
    </div>
    <div class="post">
      <div class="post-thumb" role="img" aria-label="Blog post thumbnail"><svg width="20" height="16" viewBox="0 0 20 16"><rect x="1" y="1" width="18" height="14" fill="none" stroke="#cfe9e6" stroke-width="1.5"/><path d="M3 13l5-5 3 3 2-2 4 4z" fill="#cfe9e6"/><circle cx="14" cy="5" r="1.6" fill="#cfe9e6"/></svg></div>
      <div><p>Lorem ipsum dolor sit amet, consectetur adipiscing elit</p><time>26 May, 2013</time></div>
    </div>
  </section>
</footer>
<div class="footer-bottom">
  <p class="copyright">2013 &nbsp;KELVO</p>
  <div class="social" aria-label="Social links"><span></span><span></span><span></span><span></span></div>
</div>

</body>
</html>
```